re-design the current Water Bottle

We a bottled water company and would like to re-design the water bottle, we are still working on the final vision of this product, this is why we decided to reach out to the crowd designer to seek some creative ideas..

The brand Name is "Q", the product should be elegant and modern, we would like to move away from existing cylindric water bottles. Therefore, we might consider a square base (or any other shape), please use the following dimensions:
5.5cm (L) x 5.5cm (W) X 16.5 cm (H).

We are happy to offer an extra compensation for the top 2 great designs..

Industry/Entity Type

Water Company

Font styles to use
Sans Serif
Script

Requirements
Must have
• 1- we would like to have a product that can compete with the the attached bottle..
• 2- we will welcome any colors, any out of box ideas just make sure to keep it elegant and modern..
• 3- please make sure to include the brand name in your design, as mentioned the Brand is the letter "Q" so please incorporate it in your design.
• 4- please keep in mind that you need to design the bottle lid as well, any new ideas to get out from current bottle lid will be appreciated/compensated.
• 5- Bottle material will be glass and/or PET
• 6- please note that you need to provide full graphic design in high quality format.
Should not have
• move away from existing cylindric water bottles

```html
<!DOCTYPE html>
<html lang="en">
<head>
<meta charset="utf-8">
<title>Q Artesian Water – Square Bottle</title>
<link rel="stylesheet" href="https://fonts.googleapis.com/css2?family=Josefin+Sans:wght@300;400&display=swap">
<style>
  :root {
    --backdrop: #e4e4e6;
    --water: #05b6e8;
    --water-deep: #0a9ccb;
    --water-edge: #0788b3;
    --cap: #1ba9cf;
    --cap-top: #128fb5;
    --glass: #c9dde4;
    --label-light: #f4f4f4;
    --label-mid: #c9c9c9;
    --ink-white: #ffffff;
    --ink-blue: #0ab4e6;
  }
  * { margin: 0; padding: 0; box-sizing: border-box; }
  html, body {
    width: 772px; height: 1200px; overflow: hidden;
    background: var(--backdrop);
    font-family: "Josefin Sans", sans-serif;
  }
  .canvas { position: relative; width: 772px; height: 1200px; }
  .bottle-shape { position: absolute; left: 0; top: 0; }
  .label {
    position: absolute; left: 273px; top: 466px; width: 226px; height: 435px;
    background: linear-gradient(180deg, var(--label-mid) 0%, var(--label-light) 42%, var(--label-mid) 70%, var(--label-light) 88%, var(--label-mid) 100%);
  }
  .brand-tile {
    position: absolute; left: 38px; top: 0; width: 147px; height: 174px;
    background: var(--water);
    display: flex; align-items: center; justify-content: center;
  }
  .brand-name {
    color: var(--ink-white); font-weight: 300; font-size: 118px; line-height: 1;
    padding-top: 14px;
  }
  .product-band {
    position: absolute; left: 0; top: 257px; width: 100%; height: 53px;
    background: var(--water);
    display: flex; align-items: center; justify-content: center;
  }
  .product-name {
    color: var(--ink-white); font-weight: 300; font-size: 16px; letter-spacing: 0.3px;
    text-transform: uppercase; padding-top: 3px;
  }
  .volume {
    position: absolute; left: 0; top: 385px; width: 100%; text-align: center;
    color: var(--ink-blue); font-weight: 300; font-size: 28px; line-height: 1;
  }
</style>
</head>
<body>
<main class="canvas">
  <svg class="bottle-shape" width="772" height="1200" viewBox="0 0 772 1200">
    <!-- square neck -->
    <rect class="neck" x="350" y="258" width="72" height="70" fill="var(--glass)"/>
    <!-- square-based body with chamfered shoulders -->
    <path class="body" fill="var(--water)"
      d="M350 322 L422 322 L492 410 Q499 419 499 430 L499 998 Q499 1006 491 1006 L281 1006 Q273 1006 273 998 L273 430 Q273 419 280 410 Z"/>
    <!-- side facets of the square prism -->
    <path class="facet-left" fill="var(--water-deep)"
      d="M273 430 Q273 419 280 410 L350 322 L358 322 L291 416 L291 1006 L281 1006 Q273 1006 273 998 Z"/>
    <path class="facet-right" fill="var(--water-edge)"
      d="M499 430 Q499 419 492 410 L422 322 L414 322 L481 416 L481 1006 L491 1006 Q499 1006 499 998 Z"/>
    <!-- flat square lid -->
    <rect class="lid-base" x="342" y="206" width="88" height="56" fill="var(--cap)"/>
    <rect class="lid-top" x="330" y="190" width="112" height="18" fill="var(--cap-top)"/>
    <rect class="lid-seam" x="342" y="254" width="88" height="8" fill="var(--water-deep)"/>
  </svg>

  <section class="label">
    <div class="brand-tile"><span class="brand-name">Q</span></div>
    <div class="product-band"><span class="product-name">Artesian Water</span></div>
    <p class="volume">150 M</p>
  </section>
</main>
</body>
</html>
```